Design a visually appealing layout for our company mission and values. I want to create a visually appealing 1 page flyer that presents our company mission and values to clients as well as to our internal team/staff. We will utilize the 1 page flyer in internal and external presentations about our company. We will also use the flyer in sales proposals/marketing packages.

Target Market(s)

Internal team members as well as external prospective clients, existing clients & referral partners

Industry/Entity Type

Financial Service

Colors

Designer to choose colors to be used in the design.

Requirements
Must have
• Should reflect our company brand so I have included our Pantone panel, fonts etc. I have provided our company logo as well which should be part of the branded document
Nice to have
• I would like the presentation to be useable in different formats and to different audiences so something that is more graphic/visual heavy - otherwise it's a lot of words that people don't read.
• Would like to be able to easily include in our corporate template powerpoint presentation.

```html
<!DOCTYPE html>
<html lang="en">
<head>
<meta charset="utf-8">
<title>Summit Pension Partners – Mission and Values</title>
<link href="https://fonts.googleapis.com/css2?family=Montserrat:wght@400;500;600;700;800&display=swap" rel="stylesheet">
<style>
  :root{
    --stage:#3b3b3d;
    --brand-blue:#1f6fb2;
    --headline-blue:#1b5ea8;
    --brand-green:#8cc63f;
    --navy:#163c6f;
    --navy-deep:#12325e;
    --ink:#3a3a3a;
    --white:#ffffff;
  }
  *{box-sizing:border-box;margin:0;padding:0}
  html,body{width:1200px;height:900px;overflow:hidden}
  body{background:var(--stage);font-family:"Montserrat",sans-serif;position:relative}
  .flyer{position:absolute;left:267px;top:20px;width:666px;height:860px;background:var(--white);overflow:hidden;box-shadow:0 10px 30px rgba(0,0,0,.35);display:flex;flex-direction:column}
  .top-band{height:12px;flex:none;background:var(--brand-blue)}
  .hero{position:relative;height:348px;flex:none}
  .hero-photo{position:absolute;left:0;top:0;width:320px;height:348px;background:linear-gradient(160deg,#eef0f0 0%,#d8d4cc 45%,#9aa3ad 100%)}
  .brand{position:absolute;right:30px;top:26px;text-align:right}
  .brand-name{display:flex;align-items:center;justify-content:flex-end;gap:10px;font-weight:600;font-size:17px;color:var(--brand-blue);letter-spacing:.5px}
  .brand-mark{width:16px;height:16px;background:var(--brand-green)}
  .brand-tagline{margin-top:8px;font-size:8.5px;letter-spacing:2px;color:var(--ink);font-weight:500;text-transform:uppercase}
  .mission{position:absolute;right:30px;top:120px;text-align:right}
  .mission-title{font-weight:800;font-size:36px;color:var(--headline-blue);letter-spacing:.5px}
  .mission-text{margin-top:10px;font-weight:700;font-size:17px;line-height:1.25;color:var(--ink);text-transform:uppercase}
  .green-band{height:26px;flex:none;background:var(--brand-green)}
  .values{flex:1;background:linear-gradient(180deg,var(--navy) 0%,var(--navy-deep) 100%);padding:28px 22px 0}
  .values-row{display:grid;gap:0}
  .row-four{grid-template-columns:repeat(4,1fr)}
  .row-three{grid-template-columns:repeat(3,1fr);margin-top:24px;padding:0 40px}
  .value{padding:0 12px;border-left:1px solid var(--brand-green)}
  .value:first-child{border-left:none}
  .value-icon{width:66px;height:66px;border-radius:50%;background:var(--brand-green);border:3px solid #2d7fc1;display:flex;align-items:center;justify-content:center;margin-bottom:12px}
  .value-icon svg{width:38px;height:38px;fill:none;stroke:var(--navy);stroke-width:2.4;stroke-linecap:round;stroke-linejoin:round}
  .value-title{color:var(--white);font-weight:700;font-size:11.5px;text-transform:uppercase;letter-spacing:.5px;margin-bottom:8px}
  .value-text{color:var(--white);font-size:9.5px;line-height:1.35}
</style>
</head>
<body>
<main class="flyer">
  <div class="top-band"></div>
  <section class="hero">
    <div class="hero-photo" role="img" aria-label="Photograph of a smiling woman in a denim shirt raising a fist in celebration"></div>
    <div class="brand">
      <div class="brand-name"><span class="brand-mark"></span>SUMMIT PENSION PARTNERS</div>
      <div class="brand-tagline">Reach higher. Build for tomorrow.</div>
    </div>
    <div class="mission">
      <h1 class="mission-title">OUR MISSION</h1>
      <p class="mission-text">To proactively support<br>organizations and<br>lead them toward<br>a secure future</p>
    </div>
  </section>
  <div class="green-band"></div>
  <section class="values">
    <div class="values-row row-four">
      <article class="value">
        <div class="value-icon"><svg viewBox="0 0 40 40"><circle cx="20" cy="13" r="4"/><circle cx="10" cy="26" r="4"/><circle cx="30" cy="26" r="4"/><path d="M17 16l-5 7M23 16l5 7M14 26h12"/></svg></div>
        <h2 class="value-title">Teamwork:</h2>
        <p class="value-text">Collaborating with team members, clients and partners to maintain a high level of communication, accountability and engagement to achieve our common goals</p>
      </article>
      <article class="value">
        <div class="value-icon"><svg viewBox="0 0 40 40"><path d="M6 34h28"/><rect x="9" y="24" width="5" height="10"/><rect x="18" y="18" width="5" height="16"/><rect x="27" y="11" width="5" height="23"/><path d="M8 16l8-6 6 4 10-8"/></svg></div>
        <h2 class="value-title">Financial Empowerment:</h2>
        <p class="value-text">We commit ourselves to providing the best retirement solutions to guide our clients toward financial freedom</p>
      </article>
      <article class="value">
        <div class="value-icon"><svg viewBox="0 0 40 40"><path d="M20 6a9 9 0 0 0-5 16.5V27h10v-4.5A9 9 0 0 0 20 6z"/><path d="M16 31h8M17 35h6"/></svg></div>
        <h2 class="value-title">Knowledge:</h2>
        <p class="value-text">Our team of highly trained and credentialed experts work to educate and lead our clients toward success</p>
      </article>
      <article class="value">
        <div class="value-icon"><svg viewBox="0 0 40 40"><path d="M8 30L30 8M22 8h8v8"/><path d="M8 12l6-6 6 6M14 6v14"/></svg></div>
        <h2 class="value-title">Proactivity:</h2>
        <p class="value-text">We hold ourselves accountable in anticipating regulatory changes and keeping you and your plan in compliance</p>
      </article>
    </div>
    <div class="values-row row-three">
      <article class="value">
        <div class="value-icon"><svg viewBox="0 0 40 40"><rect x="10" y="8" width="20" height="26" rx="2"/><path d="M14 14h12M14 20h12M14 26h6"/></svg></div>
        <h2 class="value-title">Dedication:</h2>
        <p class="value-text">We provide exceptional customer service and ensure that we are friendly, timely and responsive whenever corresponding with our clients</p>
      </article>
      <article class="value">
        <div class="value-icon"><svg viewBox="0 0 40 40"><path d="M20 5l12 5v9c0 8-5 13-12 16-7-3-12-8-12-16v-9z"/><path d="M14 20l4 4 8-8"/></svg></div>
        <h2 class="value-title">Security:</h2>
        <p class="value-text">With an emphasis on high technological standards, we lead you toward peace of mind that your savings and investments are protected</p>
      </article>
      <article class="value">
        <div class="value-icon"><svg viewBox="0 0 40 40"><circle cx="17" cy="17" r="9"/><path d="M24 24l9 9"/></svg></div>
        <h2 class="value-title">Transparency:</h2>
        <p class="value-text">We take pride in representing the retirement plan industry as an open, honest, and socially responsible firm with our clients</p>
      </article>
    </div>
  </section>
</main>
</body>
</html>
```